Goals Poster 2023 - Poster design of my goals and those that inspire me!

Hi there!
I'm looking to design a visually beautiful poster to represent my goals for 2023
Here is the info:
https://plinkboard.example/app/board/kT7rWqZ2mN4=/?share_link_id=418293057164
You'll see some examples of designs I like within the file too on the right! Notice the neon colours,but open to other suggestions too.,
I think "The year of No" is important.
And the rules down the bottom are particularly important.
Heres an example of a previous year: https://filenook.example/file/d/29KpRtUvWxYz3AbCdEfGhJkLmNoPqRs/view
I want to upgrade the overall design from this.
Thanks!
Ned

```html
<!DOCTYPE html>
<html lang="en">
<head>
<meta charset="utf-8">
<title>Goals Poster 2023</title>
<link rel="stylesheet" href="https://fonts.googleapis.com/css2?family=Oswald:wght@400;500;600&family=Montserrat:wght@400;500;600&display=swap">
<style>
:root{
  --ink:#000;
  --lime:#bccd5a;
  --white:#fff;
  --brand:#bccd5a;
  --minimal:#c0338a;
  --community:#a8282e;
  --skills:#9a9a9a;
  --fitness:#d9a43a;
  --income:#5a90b8;
  --love:#d05a2e;
  --spiritual:#5b4b9a;
}
*{margin:0;padding:0;box-sizing:border-box}
html,body{width:848px;height:1200px;overflow:hidden;background:var(--ink)}
.poster{position:relative;width:848px;height:1200px;background:var(--ink);color:var(--lime);font-family:Montserrat,sans-serif}
.why-band{position:absolute;left:0;top:28px;width:848px;height:39px;background:var(--lime);color:var(--white);font-family:Oswald,sans-serif;font-weight:500;font-size:21px;letter-spacing:2.6px;text-align:center;line-height:39px}
.block{position:absolute;text-align:center}
.block h2{font-family:Montserrat,sans-serif;font-weight:600;color:var(--lime);font-size:21px;letter-spacing:.5px;line-height:1}
.block p{font-size:10.6px;line-height:13px;font-weight:500}
.year-no{left:40px;width:396px;top:87px}
.year-no h2{margin-bottom:3px}
.statements{left:540px;width:250px;top:88px}
.statements h2{margin-bottom:3px}
.statements p{color:var(--white)}
.admire-title{position:absolute;left:60px;width:400px;top:206px;text-align:center;font-family:Oswald,sans-serif;font-weight:500;color:var(--white);font-size:21px;letter-spacing:3px}
.inspiring{left:560px;width:264px;top:223px}
.inspiring h2{margin-bottom:15px;font-size:21px}
.inspiring p{font-size:10.6px;line-height:13px}
.chain{position:absolute;left:0;top:0}
.section-title{position:absolute;font-family:Oswald,sans-serif;font-weight:500;color:var(--white);font-size:21px;letter-spacing:2.4px;line-height:1}
.section-title.right{text-align:right;width:300px}
.band{position:absolute;height:75px;display:flex;align-items:center;font-family:Oswald,sans-serif;font-weight:400;color:var(--white);font-size:10.3px;line-height:11.7px}
.band.left{left:67px;width:300px;padding-left:28px}
.band.right{left:505px;width:275px;padding-left:38px}
.band.brand{background:var(--brand)}
.band.minimal{background:var(--minimal)}
.band.community{background:var(--community)}
.band.skills{background:var(--skills)}
.band.fitness{background:var(--fitness)}
.band.income{background:var(--income)}
.band.love{background:var(--love)}
.band.spiritual{background:var(--spiritual)}
.art{position:absolute;left:0;top:0}
.elephant{position:absolute;left:30px;top:922px;width:172px;height:152px;background:var(--lime);border-radius:48% 52% 30% 40%/55% 60% 20% 20%}
.rules{left:40px;width:768px;top:978px}
.rules h2{margin-bottom:12px}
.rules p{font-size:10.6px;line-height:13.2px}
</style>
</head>
<body>
<main class="poster">
  <div class="why-band">WHY: LIVE EVERYDAY WITH INTEGRITY AND PRODUCE AN OUTPUT ID ADMIRE</div>

  <section class="block year-no">
    <h2>THE YEAR OF "NO"</h2>
    <p>Deep minimalism - remove EVERYTHING that can be removed.<br>
    No coaching - unless I get upside or am generating content<br>
    No travel for events - Travel ok (w/ Tessa, see family,<br>
    building my core community, meditation retreat)<br>
    No random rabbit-holes of Chirpline, email subscriptions, etc..</p>
  </section>

  <section class="block statements">
    <h2>THE STATEMENTS:</h2>
    <p>"What you can be you must be"<br>What would Harlan Voss do?</p>
  </section>

  <div class="admire-title">TO BE SOMEONE I'D FULLY ADMIRE</div>

  <svg class="chain" width="848" height="400" viewBox="0 0 848 400">
    <g fill="none" stroke="var(--lime)" stroke-width="2.5">
      <circle cx="103" cy="300" r="56"/><circle cx="206" cy="300" r="56"/><circle cx="309" cy="300" r="56"/><circle cx="412" cy="300" r="56"/><circle cx="515" cy="300" r="56"/>
    </g>
    <g fill="var(--ink)">
      <circle cx="103" cy="300" r="54.6"/><circle cx="206" cy="300" r="54.6"/><circle cx="309" cy="300" r="54.6"/><circle cx="412" cy="300" r="54.6"/><circle cx="515" cy="300" r="54.6"/>
    </g>
    <circle cx="103" cy="300" r="43" fill="#a9bd3f" role="img" aria-label="Portrait of Rory Halvorsen"/>
    <circle cx="206" cy="300" r="43" fill="#d9a43a" role="img" aria-label="Portrait of Dane Whitcombe"/>
    <circle cx="309" cy="300" r="43" fill="#4f8fbf" role="img" aria-label="Portrait of Corin Vasquez"/>
    <circle cx="412" cy="300" r="43" fill="#b3262e" role="img" aria-label="Portrait of Milo Ferrant"/>
    <circle cx="515" cy="300" r="43" fill="#c93a93" role="img" aria-label="Portrait of Jasper Ellory"/>
    <defs>
      <path id="arc1" d="M52,300 A51,51 0 0 0 154,300"/>
      <path id="arc2" d="M155,300 A51,51 0 0 0 257,300"/>
      <path id="arc3" d="M258,300 A51,51 0 0 0 360,300"/>
      <path id="arc4" d="M361,300 A51,51 0 0 0 463,300"/>
      <path id="arc5" d="M464,300 A51,51 0 0 0 566,300"/>
    </defs>
    <g fill="var(--lime)" font-family="Montserrat,sans-serif" font-size="7.5" font-weight="500" letter-spacing=".4">
      <text><textPath href="#arc1" startOffset="50%" text-anchor="middle">RORY HALVORSEN</textPath></text>
      <text><textPath href="#arc2" startOffset="50%" text-anchor="middle">DANE WHITCOMBE</textPath></text>
      <text><textPath href="#arc3" startOffset="50%" text-anchor="middle">CORIN VASQUEZ</textPath></text>
      <text><textPath href="#arc4" startOffset="50%" text-anchor="middle">MILO FERRANT</textPath></text>
      <text><textPath href="#arc5" startOffset="50%" text-anchor="middle">JASPER ELLORY</textPath></text>
    </g>
  </svg>

  <section class="block inspiring">
    <h2>INSPIRING PERSON :</h2>
    <p>Impact<br>Fitness<br>Thought leader<br>Financially Liberated &amp; successful<br>Business where passion is<br>Amazing community<br>Great ralationship</p>
  </section>

  <div class="section-title" style="left:68px;top:385px">PERSONAL BRAND</div>
  <div class="band left brand" style="top:413px">Collectively over 500,000 across Chirpline,<br>Workweb, Streamly, Clipzy &amp; Snapgrid<br>26 videos I'm very proud of</div>

  <div class="section-title" style="left:68px;top:517px">DEEP MINIMALISATION</div>
  <div class="band left minimal" style="top:545px">Remove as many objects as possible<br>Close open loops in my brain<br>Remove as many decisions as possible.<br>Automate as much as possible - food, fitness, calendar<br>Limit number of projects allowed<br>Calendar sweep</div>

  <div class="section-title" style="left:68px;top:649px">COMMUNITY</div>
  <div class="band left community" style="top:677px">Hosting brunch every ~2 weeks<br>Hosting 4 retreats<br>2 Nothing spared's<br>2 Just amazing humans<br>Hosting ~4 big events</div>

  <div class="section-title" style="left:68px;top:782px">SKILLS</div>
  <div class="band left skills" style="top:810px">Learn conversational Swedish<br>DJ at house parties</div>

  <div class="section-title right" style="left:480px;top:452px">FITNESS</div>
  <div class="band right fitness" style="top:479px">85kg, 10% bf &nbsp;- &nbsp;Follow blueprint! &nbsp;- &nbsp;Handstand 30 secs<br>~2-3 meals per day cooked for me - clear nutrition plan<br>90 day no alcohol challenge / transformation.<br>Exercise 6 days a week<br>Clear goals with KPIs broken down by quarter and measured<br>on my wall in gym. (Same with friends).</div>

  <div class="section-title right" style="left:480px;top:584px">INCOME</div>
  <div class="band right income" style="top:612px">Sold Loudframe, NW +$XXmil<br>Build ~$Xxxmil+ income with Loudframe US,<br>and minority purchase in cash-flowing assets<br>Start personal brand agency and scale to $XXXk/mo+</div>

  <div class="section-title right" style="left:480px;top:716px">LOVE</div>
  <div class="band right love" style="top:744px">Plan a fun date with Tessa monthly<br>Tantra exploration<br>Relationship coach</div>

  <div class="section-title right" style="left:480px;top:848px">SPIRITUAL</div>
  <div class="band right spiritual" style="top:876px">Do one meditation retreat<br>Do one Tantra workshop</div>

  <svg class="art" width="848" height="1000" viewBox="0 0 848 1000">
    <polygon fill="var(--lime)" points="432,427 512,427 466,555 500,555 455,690 490,690 445,826 476,826 359,975 398,818 368,818 410,688 378,688 420,558 388,558"/>
    <g fill="var(--white)">
      <circle cx="365" cy="451" r="47"/><circle cx="365" cy="583" r="47"/><circle cx="365" cy="715" r="47"/><circle cx="365" cy="847" r="47"/>
      <circle cx="480" cy="516" r="47"/><circle cx="480" cy="648" r="47"/><circle cx="480" cy="781" r="47"/><circle cx="480" cy="913" r="47"/>
    </g>
    <g font-family="Montserrat,sans-serif" font-size="7.5" font-weight="600" fill="#333" text-anchor="middle">
      <text x="365" y="429">Clipzy</text><text x="365" y="440">Streamly</text><text x="365" y="451">Workweb</text><text x="365" y="462">Snapgrid</text><text x="365" y="473">Chirpline</text>
    </g>
    <g fill="#111">
      <rect x="446" y="512" width="68" height="8" rx="2"/>
      <rect x="452" y="499" width="6" height="34" rx="2"/><rect x="460" y="502" width="5" height="28" rx="2"/>
      <rect x="502" y="499" width="6" height="34" rx="2"/><rect x="495" y="502" width="5" height="28" rx="2"/>
    </g>
    <g fill="none" stroke="#111" stroke-width="4">
      <circle cx="343" cy="588" r="8"/><circle cx="358" cy="603" r="8"/>
      <line x1="349" y1="583" x2="385" y2="562"/><line x1="353" y1="597" x2="374" y2="558"/>
    </g>
    <text x="480" y="668" text-anchor="middle" font-family="Montserrat,sans-serif" font-weight="600" font-size="56" fill="#a9bd3f">$</text>
    <circle cx="365" cy="715" r="34" fill="#e8a23a" role="img" aria-label="Icon of a group of people"/>
    <path d="M480,805 L454,778 C444,766 452,752 466,753 C473,754 478,759 480,764 C482,759 487,754 494,753 C508,752 516,766 506,778 Z" fill="#c8262c"/>
    <g fill="#c9962a">
      <circle cx="338" cy="838" r="4"/><circle cx="350" cy="826" r="4"/><circle cx="365" cy="821" r="4"/><circle cx="380" cy="826" r="4"/><circle cx="392" cy="838" r="4"/>
    </g>
    <path d="M343,862 A23,23 0 0 1 387,862" fill="none" stroke="#1d2f4a" stroke-width="4"/>
    <circle cx="480" cy="913" r="34" fill="#e8903a" role="img" aria-label="Icon of a person meditating"/>
  </svg>

  <div class="elephant" role="img" aria-label="Silhouette of an elephant"></div>

  <section class="block rules">
    <h2>YEARLY RULES</h2>
    <p>Yearly rules:<br>
    No Streamly, TV, Movies, Flickbox &amp; games unless in the company of friends<br>
    No social media (possible exception tbd is unless working out by my self)<br>
    Get Priya to post weekly Snapgrid stories on all my channels<br>
    Get Priya to review message requests on snapgrid/chirpline<br>
    No eating off plan unless in the company of 4 or more people<br>
    No caffeine<br>
    No alcohol<br>
    No additional projects - Unless the TOTAL time involvement is &lt; 30 hours in 2023 and the business is mission driven.<br>
    Don't even explore other ideas. You got plenty to work on and solve mate. And I must convince Callum &amp; Devin its worthy of my time.<br>
    Audiobooks before bed instead of podcasts<br>
    Build friend CRM, actively reach out to interesting people every month</p>
  </section>
</main>
</body>
</html>
```